Badminton Club

Create a web flyer for the advertisement of the club. I'm attaching the old version for your reference. Need something more modern, fresh, dynamic.

```html
<!DOCTYPE html>
<html lang="en">
<head>
<meta charset="utf-8">
<title>Badminton Club Flyer</title>
<link rel="stylesheet" href="https://fonts.googleapis.com/css2?family=Bebas+Neue&family=Oswald:wght@600;700&family=Roboto:wght@400;500;700&display=swap">
<style>
:root{
  --blue:#4472c4;
  --blue-deep:#2f5aa8;
  --title-blue:#3a66c2;
  --white:#ffffff;
  --ink:#111111;
  --stage:#c4c4c4;
}
*{margin:0;padding:0;box-sizing:border-box}
html,body{width:1200px;height:1200px;overflow:hidden}
body{background:var(--stage);position:relative;font-family:"Roboto",Arial,sans-serif}

.flyer{position:absolute;background:var(--blue);overflow:hidden}
.flyer--front{left:99px;top:257px;width:467px;height:660px}
.flyer--faq{left:636px;top:258px;width:460px;height:652px}

/* front */
.schedule{position:absolute;left:12px;top:159px;width:99px;height:93px;border:2px solid var(--white);border-radius:8px;color:var(--white);font-family:"Oswald",sans-serif;font-weight:600;text-align:center;padding-top:30px;line-height:1.15}
.schedule .day{font-size:12px;display:block}
.schedule .hours{font-size:10.5px;display:block;margin-bottom:3px}
.schedule-clock{position:absolute;left:35px;top:131px;width:54px;height:54px}

.headline{position:absolute;color:var(--white);font-family:"Bebas Neue",sans-serif;font-weight:400;line-height:1;white-space:nowrap;transform-origin:0 80%}
.headline--club{left:285px;top:183px;font-size:78px;transform:rotate(-8.5deg)}
.headline--badminton{left:69px;top:284px;font-size:100px;transform:rotate(-8.6deg)}
.rule-line{position:absolute;left:60px;top:281px;width:222px;height:1.5px;background:var(--white);transform:rotate(-9.7deg);transform-origin:left center}

.ribbon{position:absolute;left:73px;top:381px;width:362px;height:37px;background:var(--white);transform:rotate(-9.3deg);transform-origin:left center;box-shadow:0 6px 10px rgba(0,0,0,.25);color:var(--blue);font-weight:700;font-size:15px;display:flex;align-items:center;padding-left:10px;white-space:nowrap}

.register-rail{position:absolute;left:255px;top:437px;width:1.5px;height:117px;background:var(--white)}
.register-tag{position:absolute;left:273px;top:436px;width:110px;height:19px;background:var(--white);color:var(--blue);font-size:10.5px;font-weight:500;letter-spacing:.3px;display:flex;align-items:center;justify-content:center}
.register-link{position:absolute;left:383px;top:445px;width:52px;height:1.5px;background:var(--white)}
.register-dot{position:absolute;left:432px;top:442px;width:7px;height:7px;border-radius:50%;background:var(--white)}
.register-line{position:absolute;left:295px;color:var(--white);font-size:10.5px;white-space:nowrap}
.register-line strong{font-weight:700}
.register-icon{position:absolute;width:13px;height:13px}

.front-footer{position:absolute;left:0;top:583px;width:467px;height:65px;background:var(--white)}
.partner{position:absolute;display:flex;align-items:center;gap:4px;color:var(--ink);font-size:8px;font-weight:700;line-height:1.15}
.partner-mark{width:10px;height:10px;background:var(--blue);flex:none}
.partner-mark--round{border-radius:50%}
.partner-note{position:absolute;left:90px;top:44px;font-size:5.5px;color:var(--ink);line-height:1.2;text-align:center;width:100px}
.footer-divider{position:absolute;left:264px;top:6px;width:1.5px;height:50px;background:var(--blue)}
.venue-pin{position:absolute;left:279px;top:12px;width:12px;height:16px}
.venue{position:absolute;left:300px;top:12px;font-size:10.5px;font-weight:500;line-height:13.5px;color:var(--ink);font-style:normal}

/* faq */
.faq-head{position:absolute;left:0;top:12px;width:460px;height:59px;background:var(--white);display:flex;align-items:center;justify-content:center}
.faq-title{font-family:"Bebas Neue",sans-serif;font-weight:400;font-size:40px;color:var(--title-blue);letter-spacing:-1px;line-height:1}

.court-photo{position:absolute;left:0;top:420px;width:460px;height:232px;background:linear-gradient(180deg,rgba(47,90,168,0) 0%,rgba(47,90,168,.55) 40%,#2a4f96 100%)}
.court-photo::after{content:"";position:absolute;left:250px;top:120px;width:200px;height:90px;border-radius:50%;background:radial-gradient(ellipse at center,rgba(230,238,250,.55),rgba(230,238,250,0) 70%)}

.shuttle-deco{position:absolute;width:46px;height:46px;border-radius:10px;background:rgba(255,255,255,.12)}

.timeline{position:absolute;left:16px;top:102px;width:1.5px;height:424px;background:var(--white)}
.faq-dot{position:absolute;left:12.5px;width:8px;height:8px;border-radius:50%;background:var(--white)}
.faq-q,.faq-a{position:absolute;left:29px;color:var(--white);white-space:nowrap;line-height:12px}
.faq-q{font-weight:700;font-size:9.8px;letter-spacing:.1px}
.faq-a{font-weight:400;font-size:9.2px}
</style>
</head>
<body>

<section class="flyer flyer--front" aria-label="Badminton Club flyer front">
  <div class="schedule">
    <span class="day">Every Tuesday</span>
    <span class="hours">18h30 to 22h00</span>
    <span class="day">Every Thursday</span>
    <span class="hours">18h30 to 20h00</span>
  </div>
  <svg class="schedule-clock" viewBox="0 0 54 54" aria-hidden="true">
    <circle cx="27" cy="27" r="25" fill="#ffffff"/>
    <circle cx="27" cy="27" r="19" fill="none" stroke="#4472c4" stroke-width="4"/>
    <path d="M27 16 V28 L34 34" fill="none" stroke="#4472c4" stroke-width="3.5" stroke-linecap="round"/>
  </svg>

  <div class="rule-line"></div>
  <h1 class="headline headline--club">CLUB</h1>
  <div class="headline headline--badminton">BADMINTON</div>
  <div class="ribbon">Badminton Club of the Lakeside Union in Geneva</div>

  <div class="register-rail"></div>
  <div class="register-tag">HOW TO REGISTER</div>
  <div class="register-link"></div>
  <div class="register-dot"></div>

  <svg class="register-icon" style="left:274px;top:469px" viewBox="0 0 14 14" aria-hidden="true">
    <g fill="none" stroke="#ffffff" stroke-width="1">
      <circle cx="7" cy="7" r="6"/><ellipse cx="7" cy="7" rx="2.6" ry="6"/><path d="M1 7H13M2 4H12M2 10H12"/>
    </g>
  </svg>
  <div class="register-line" style="top:467px">www.<strong>shortlink.example/bclug19</strong></div>
  <div class="register-line" style="top:482px">Please send signed from to the</div>
  <svg class="register-icon" style="left:272px;top:502px;height:10px" viewBox="0 0 14 10" aria-hidden="true">
    <rect x="0.5" y="0.5" width="13" height="9" fill="none" stroke="#ffffff"/><path d="M0.5 0.5 L7 6 L13.5 0.5" fill="none" stroke="#ffffff"/>
  </svg>
  <div class="register-line" style="top:500px;left:293px"><strong>bclug19@mailbox.example</strong></div>
  <div class="register-line" style="top:516px;left:293px">and pay the fees</div>

  <footer class="front-footer">
    <div class="partner" style="left:38px;top:18px;width:50px"><span class="partner-mark"></span><span>Sports Union Geneva</span></div>
    <div class="partner" style="left:98px;top:10px;width:92px;text-align:center">Lakeside Staff Sports Board</div>
    <div class="partner-note">Maison du Lac, CH-1200 Genève<br>022 000 00 00</div>
    <div class="partner" style="left:193px;top:26px"><span class="partner-mark partner-mark--round"></span><span>LUG Club</span></div>
    <div class="footer-divider"></div>
    <svg class="venue-pin" viewBox="0 0 12 16" aria-hidden="true">
      <path d="M6 0.5C3 0.5 0.8 2.8 0.8 5.6C0.8 9.5 6 15.5 6 15.5S11.2 9.5 11.2 5.6C11.2 2.8 9 0.5 6 0.5Z" fill="#4472c4"/>
      <circle cx="6" cy="5.6" r="2" fill="#ffffff"/>
    </svg>
    <address class="venue">Collège des Tilleuls -Salle C<br>avenue des Platanes, 12<br>1200 Genève</address>
  </footer>
</section>

<section class="flyer flyer--faq" aria-label="Frequently asked questions">
  <div class="faq-head"><h2 class="faq-title">FREQUENTLY ASKED QUESTIONS</h2></div>

  <div class="court-photo" role="img" aria-label="Photo of a shuttlecock resting on a racket on a blurred indoor court"></div>

  <div class="shuttle-deco" style="left:370px;top:111px" role="img" aria-label="Shuttlecock outline decoration"></div>
  <div class="shuttle-deco" style="left:227px;top:274px" role="img" aria-label="Shuttlecock outline decoration"></div>
  <div class="shuttle-deco" style="left:430px;top:287px" role="img" aria-label="Shuttlecock outline decoration"></div>
  <div class="shuttle-deco" style="left:310px;top:402px" role="img" aria-label="Shuttlecock outline decoration"></div>
  <div class="shuttle-deco" style="left:432px;top:501px" role="img" aria-label="Shuttlecock outline decoration"></div>
  <div class="shuttle-deco" style="left:0;top:574px" role="img" aria-label="Shuttlecock outline decoration"></div>

  <div class="timeline"></div>

  <span class="faq-dot" style="top:98px"></span>
  <p class="faq-q" style="top:96px">CAN I COME AND TRY WITHOUT REGISTERING?</p>
  <p class="faq-a" style="top:114px">Yes, you can come and try once if courts are not full. Ask us ahead.</p>

  <span class="faq-dot" style="top:142px"></span>
  <p class="faq-q" style="top:140px">WHAT EQUIPMENT DO I NEED TO ATTEND THE SESS</p>
  <p class="faq-a" style="top:158px">You need a badminton racket and shoes with non–marking soles.</p>

  <span class="faq-dot" style="top:182px"></span>
  <p class="faq-q" style="top:180px">WHAT EQUIPMENT DOES THE CLUB PROVIDE?</p>
  <p class="faq-a" style="top:193px">The Club provides the venue, the net and the shuttlecocks.</p>

  <span class="faq-dot" style="top:216px"></span>
  <p class="faq-q" style="top:214px">WHAT IS THE ANNUAL FEE?</p>
  <p class="faq-a" style="top:227px">Full season is CHF 140 and half-season (09/2019-01/2020 ) costs CHF 90 (120 and 80 for</p>
  <p class="faq-a" style="top:240px">duespaying members of the LUG Staff Council). For LU interns and students it is only CHF 50.</p>

  <span class="faq-dot" style="top:265px"></span>
  <p class="faq-q" style="top:263px">WHEN DOES THE SEASON START?</p>
  <p class="faq-a" style="top:276px">Tuesday, 3 September 2019.</p>

  <span class="faq-dot" style="top:303px"></span>
  <p class="faq-q" style="top:301px">WHEN DOES THE SEASON END?</p>
  <p class="faq-a" style="top:314px">Thursday, 11 June 2020.</p>

  <span class="faq-dot" style="top:342px"></span>
  <p class="faq-q" style="top:340px">WHAT IF I CAN ATTEND ONLY ONCE A WEEK?</p>
  <p class="faq-a" style="top:354px">It does not impact the fee. However, we ask you to inform us in advance on your participation.</p>

  <span class="faq-dot" style="top:382px"></span>
  <p class="faq-q" style="top:380px">HOW CAN I PAY?</p>
  <p class="faq-a" style="top:393px">Via online transfer or at the post office to:</p>
  <p class="faq-a" style="top:406px">Club de Badminton de l'Union du Lac à Genève</p>
  <p class="faq-a" style="top:419px">IBAN CH1200880000123456789A ; BIC LKBKCHGG10A</p>

  <span class="faq-dot" style="top:445px"></span>
  <p class="faq-q" style="top:443px">IS THERE BADMINTON ALL YEAR?</p>
  <p class="faq-a" style="top:456px">No. The gym will be closed during Geneva school holidays. We organize social events then ☺.</p>

  <span class="faq-dot" style="top:484px"></span>
  <p class="faq-q" style="top:482px">CAN I REGISTER IF I AM AN INTERN/CONSULTANT OR DO NOT WORK FOR THE LU?</p>
  <p class="faq-a" style="top:495px">Yes, the Club is open for everybody. You can be a member if you do not work for the LU.</p>

  <span class="faq-dot" style="top:522px"></span>
  <p class="faq-q" style="top:520px">HOW MANY PEOPLE ARE IN THE CLUB?</p>
  <p class="faq-a" style="top:534px">The Club can have up to 40 members.</p>
</section>

</body>
</html>
```